Compatible Printer Cartridge Box Design

We are looking to package toners cartridges & ink cartridges that we recycle in our shop. Attached is a doc file that tell what design we want, ideas, and sizes.

Unlike other compatible toner cartridges that are manufactured from scratch, LUMO Print Consumables are made from recycled original OEM print toners. This will maintain the original OEM parts inside the cartridge, maintain the original cartridge tolerance, ensure proper cartridge alignment in the printer, and minimize human error.

Project Deadline Extended
Reason: Hi to all, I am not satisfied with the current designs. I will extend for more 5 days and increase the budget. Thank You

Target Market(s)

Construction Companies, Banks, Hospitals, Oil Companies, Insurance Companies

Industry/Entity Type

Printer

Font styles to use
Other font styles liked:
• Calibri

Requirements
Must have
• The file must be in .ai format. So we can change the size of the box any time later.
• The file must be ready to be given to the printing press (specially the die cut). No any alteration must be made from our side.
• Since there are different models of cartridges, one side of the box must be left for a label that state the cartridge model, bar code, and compatible printers.
• The theme of the box must be quoted from our company logo, specially the colors. We prefer bold corporate design. Maybe with a woman on it (Not a must), and something related to protecting the environment. Avoid using the carton brown color.
• We prefer toner box that Can be opened from the top with that cartoon lock. For the ink cartridge, we would like to look like the zx one.
Nice to have
• Maybe with a woman on it (Not a must), and something related to protecting the environment.
Should not have
• Avoid using the carton brown color.

```html
<!DOCTYPE html>
<html lang="en">
<head>
<meta charset="utf-8">
<title>LUMO Premium Toner – Box Dieline</title>
<link rel="stylesheet" href="https://fonts.googleapis.com/css2?family=Oswald:wght@500;700&family=Carlito:wght@400;700&family=Courgette&display=swap">
<style>
  :root{
    --green:#8cb12f;
    --green-dark:#6f9324;
    --orange:#e38f25;
    --orange-light:#f2b866;
    --black:#0b0b0b;
    --charcoal:#3b3b3b;
    --white:#ffffff;
    --page:#f1f1f1;
    --forest-dark:#1f2f1a;
    --forest-mid:#4f6b2c;
    --forest-light:#8fae43;
  }
  *{box-sizing:border-box;margin:0;padding:0}
  html,body{width:1200px;height:1000px;overflow:hidden}
  body{background:var(--page);position:relative;font-family:"Carlito","Calibri",sans-serif;color:var(--white)}
  .dieline{position:absolute;left:0;top:0;width:1200px;height:1000px}
  .panel{position:absolute;overflow:hidden}

  /* display type */
  .title{font-family:"Oswald",sans-serif;font-weight:700;line-height:.92;text-transform:uppercase;color:var(--white);white-space:nowrap}
  .title .big{display:block;font-size:28px;letter-spacing:-.5px}
  .title .mid{display:block;font-size:11px;font-weight:500}
  .title .sm{display:block;font-size:15px}
  .script{font-family:"Courgette",cursive;color:var(--white);white-space:nowrap}
  .model{font-family:"Carlito",sans-serif;line-height:1;color:var(--white)}
  .model .label{display:block;font-size:7px;letter-spacing:.3px}
  .model .code{display:block;font-size:15px}

  /* brand lockup: plain square + name */
  .brand{position:absolute;display:flex;flex-direction:column;align-items:flex-start}
  .brand .square{background:var(--orange)}
  .brand .name{font-family:"Carlito",sans-serif;font-weight:700;color:var(--green);line-height:1}

  .paw{position:absolute;border-radius:50%}
  .badges{position:absolute;display:flex;gap:6px}
  .badge{width:22px;height:22px;border-radius:50%;background:var(--green);border:2px solid var(--white)}

  /* lid */
  .lid{left:175px;top:75px;width:358px;height:135px;background:var(--black);border-radius:10px 10px 0 0}
  .lid .corner{position:absolute;inset:0;background:var(--orange);clip-path:polygon(262px 135px,358px 135px,358px 50px)}
  .lid .slogan{position:absolute;right:10px;top:33px;font-size:7px;font-weight:700;text-align:right;line-height:1.15}
  .lid .title{position:absolute;left:314px;top:86px}
  .lid .title .big{font-size:16px}.lid .title .mid{font-size:8px}.lid .title .sm{font-size:9px}

  /* side flaps */
  .flap-left{left:67px;top:138px;width:108px;height:72px;background:var(--green);border-radius:14px 0 0 0}
  .flap-right{left:540px;top:138px;width:100px;height:72px;background:var(--orange);border-radius:0 14px 0 0}
  .glue{left:42px;top:210px;width:25px;height:158px;background:var(--white);border:1px solid #e2e2e2;border-right:none}

  /* left side */
  .side-left{left:67px;top:210px;width:108px;height:158px;background:var(--green)}
  .side-left .model{position:absolute;left:8px;top:16px}
  .side-left .model .label{font-size:8px}.side-left .model .code{font-size:16px}
  .side-left .title{position:absolute;left:62px;top:102px}
  .side-left .title .big{font-size:18px}.side-left .title .mid{font-size:8px}.side-left .title .sm{font-size:10px}

  /* front */
  .front{left:175px;top:210px;width:358px;height:158px;background:var(--green)}
  .front .forest{position:absolute;inset:0;background:linear-gradient(160deg,var(--forest-dark) 0%,var(--forest-mid) 55%,var(--forest-light) 100%);clip-path:polygon(262px 0,358px 0,358px 158px,125px 158px)}
  .front .title{position:absolute;left:19px;top:15px}
  .front .save{position:absolute;left:95px;top:20px;font-size:8px;line-height:1.15;text-transform:uppercase}
  .front .script{position:absolute;left:22px;top:86px;font-size:14px;transform:rotate(-8deg);transform-origin:left center}
  .front .model{position:absolute;left:22px;top:124px}
  .front .compat{position:absolute;right:6px;top:90px;font-size:6px;text-align:right;line-height:1.2}
  .front .badges{right:12px;bottom:12px}

  /* right side */
  .side-right{left:533px;top:210px;width:107px;height:158px;background:var(--orange)}
  .side-right .title{position:absolute;left:66px;top:10px}
  .side-right .title .big{font-size:15px}.side-right .title .mid{font-size:7px}.side-right .title .sm{font-size:9px}
  .benefits{position:absolute;left:4px;top:92px;width:98px;background:var(--white);padding:3px}
  .benefits h2{font-size:6px;font-weight:700;color:var(--black);margin-bottom:3px;white-space:nowrap}
  .benefits li{list-style:none;background:var(--orange-light);color:var(--black);font-size:4px;padding:2px 3px;margin-bottom:2px;border-left:2px solid var(--orange);white-space:nowrap;overflow:hidden}

  /* bottom dust band */
  .band{left:94px;top:368px;width:546px;height:112px;background:var(--black)}

  /* back (printed upside down) */
  .back{left:175px;top:480px;width:358px;height:156px;background:var(--green);transform:rotate(180deg)}
  .back .corner{position:absolute;inset:0;background:var(--orange);clip-path:polygon(0 0,203px 0,43px 156px,0 156px)}
  .back .web{position:absolute;left:63px;top:134px;font-size:9px;letter-spacing:.3px}
  .back .why{position:absolute;left:8px;top:70px;width:120px;font-size:4px;line-height:1.35;color:var(--black)}
  .back .why h3{font-size:5px;font-weight:700;margin-bottom:2px}
  .back .why p{margin-bottom:2px}
  .back .maker{position:absolute;left:233px;top:88px;font-size:4px;line-height:1.3;color:var(--black)}
  .back .maker .code{font-size:7px;font-weight:700}
  .back .badges{left:228px;top:14px}
</style>
</head>
<body>
<main class="dieline" aria-label="LUMO Premium Toner box dieline">

  <section class="panel lid">
    <div class="corner"></div>
    <div class="brand" style="left:12px;top:35px">
      <span class="square" style="width:52px;height:44px"></span>
      <span class="name" style="font-size:12px;margin-top:3px">Lumora</span>
    </div>
    <div class="paw" role="img" aria-label="paw print decoration" style="left:132px;top:52px;width:58px;height:56px;background:var(--charcoal)"></div>
    <div class="paw" role="img" aria-label="paw print decoration" style="left:243px;top:25px;width:32px;height:34px;background:var(--charcoal)"></div>
    <p class="slogan">YOU CAN PRINT MORE<br>WHILE PAYING LESS</p>
    <h2 class="title"><span class="big">LUMO</span><span class="mid">Premium</span><span class="sm">Toner</span></h2>
  </section>

  <div class="panel flap-left"></div>
  <div class="panel flap-right"></div>
  <div class="panel glue"></div>

  <section class="panel side-left">
    <div class="paw" role="img" aria-label="faint paw print decoration" style="left:10px;top:-20px;width:70px;height:80px;background:rgba(255,255,255,.22)"></div>
    <p class="model"><span class="label">MODEL NO</span><span class="code">ABC12G</span></p>
    <div class="brand" style="left:8px;top:120px">
      <span class="square" style="width:22px;height:18px"></span>
      <span class="name" style="font-size:6px;color:var(--white);margin-top:1px">Lumora</span>
    </div>
    <h2 class="title"><span class="big">LUMO</span><span class="mid">Premium</span><span class="sm">Toner</span></h2>
  </section>

  <section class="panel front">
    <div class="forest" role="img" aria-label="forest photograph with tall trees and green undergrowth"></div>
    <h1 class="title"><span class="big">LUMO</span><span class="mid">Premium</span><span class="sm">Toner</span></h1>
    <p class="save">Save up to 70% of your<br>printing expenses</p>
    <p class="script">Printing Happy</p>
    <p class="model"><span class="label">MODEL NO</span><span class="code">ABC12G</span></p>
    <div class="paw" role="img" aria-label="white paw print decoration" style="left:125px;top:88px;width:48px;height:52px;background:var(--white)"></div>
    <div class="paw" role="img" aria-label="white paw print decoration" style="left:222px;top:44px;width:28px;height:30px;background:var(--white)"></div>
    <div class="brand" style="left:287px;top:15px">
      <span class="square" style="width:58px;height:44px"></span>
      <span class="name" style="font-size:11px;margin-top:2px">Lumora</span>
    </div>
    <p class="compat">COMPATIBLE<br>ZX/SAMVO/KANTO</p>
    <div class="badges" aria-label="certification badges">
      <span class="badge"></span><span class="badge"></span><span class="badge"></span><span class="badge"></span>
    </div>
  </section>

  <section class="panel side-right">
    <div class="paw" role="img" aria-label="faint paw print decoration" style="left:10px;top:4px;width:44px;height:52px;background:rgba(255,255,255,.3)"></div>
    <h2 class="title"><span class="big">LUMO</span><span class="mid">Premium</span><span class="sm">Toner</span></h2>
    <div class="benefits">
      <h2>Benefits of Using LUMO Premium</h2>
      <ul>
        <li>You can save up to 70% of your printing expenses</li>
        <li>You can print more while paying less</li>
        <li>You reduce your environmental footprint</li>
        <li>You get peace of mind by our 3 years warranty</li>
      </ul>
    </div>
  </section>

  <div class="panel band"></div>

  <section class="panel back">
    <div class="corner"></div>
    <p class="web">www.lumora-print.com</p>
    <div class="why">
      <h3>Why LUMO Premium Cartridges?</h3>
      <p>LUMO cartridges are rebuilt from original OEM shells, so every part keeps its factory fit and tolerance. Each unit is cleaned, refilled and tested page by page before it leaves our shop.</p>
      <p>Reusing original parts keeps waste out of landfill and lowers your cost per page without losing print quality.</p>
    </div>
    <div class="brand" style="left:233px;top:62px">
      <span class="square" style="width:18px;height:15px"></span>
      <span class="name" style="font-size:5px;margin-top:1px;color:var(--white)">Lumora</span>
    </div>
    <div class="maker">
      <p>Lumora Print &amp; Office Supplies</p>
      <p>Dubai, United Arab Emirates</p>
      <p class="code">ABC12G</p>
    </div>
    <div class="badges" aria-label="certification badges">
      <span class="badge"></span><span class="badge"></span><span class="badge"></span><span class="badge"></span>
    </div>
  </section>

</main>
</body>
</html>
```